Flyer for Daycare

A Flyer for family group daycare
Specfs:
- One side english / Another Side spanish(the text for both sides is below)
- The flyer is for printing in 5" x 7" or 5.5" x 8.5"
- The address and phone number is the most important
Logo(see the attachment)
NYC Licensed
Children from 6 Weeks to 12 years old
Accepting All the Programs( TPB, OMW) and Private
CPR & First Aid Certified
Full Time, Part Time and After School
----------------------------------------------------------------------------
Provide Homework Assistance
Potty Training
Outdoor Activities
Nutritional Meals & Snack
Baby Wipes
Text in Spanish
Licencia por el estado de NY
Niños de 6 semanas a 12 años
Aceptando Todos los Programas (TPB, OMW) y Privado
Certificación en CPR y Primeros Auxilios
Tiempo completo, tiempo parcial y después de la escuela
----------------------------------------------------------------------------------------------
Actividades al aire libre
Asistencia con la tarea
Entrenamiento para ir al baño
Desayunos, Comidas y refrigerios nutricionales
Toallitas para bebé
582 E 416th ST
APT 4C
Bronx, NY, 10587
ig: @lumokidcare
555-718-2043
Target Market(s)
LAtin and Black, Bronx NY Area
Industry/Entity Type
Daycare service
Look and feel

```html
<!DOCTYPE html>
<html lang="en">
<head>
<meta charset="utf-8">
<title>Lumo Kid Care – Bilingual Flyer</title>
<link href="https://fonts.googleapis.com/css2?family=Oswald:wght@600&family=Roboto:wght@500;700;900&family=Roboto+Slab:wght@700&display=swap" rel="stylesheet">
<style>
  :root{
    --sky:#1f9cf5;
    --blue:#1c4fc9;
    --navy:#1a2d8c;
    --ink:#1b3a9b;
    --yellow:#ffd21f;
    --orange:#f7941d;
    --red:#e52421;
    --red-deep:#c8161a;
    --cloud:#8fdcff;
    --aqua:#29b6f6;
    --white:#ffffff;
    --page:#a3a3a3;
  }
  *{margin:0;padding:0;box-sizing:border-box}
  html,body{width:805px;height:1200px;overflow:hidden;background:var(--page)}

  /* each side is built at 805 × 1127 and scaled onto the sheet */
  .flyer{position:absolute;top:335px;width:805px;height:1127px;background:var(--white);overflow:hidden;font-family:"Roboto",Arial,sans-serif;transform:scale(.47);transform-origin:0 0;box-shadow:0 4px 14px rgba(0,0,0,.35)}
  .flyer--en{left:16px}
  .flyer--es{left:411px}

  .backdrop{position:absolute;left:0;top:0;width:805px;height:500px}
  .age-tab{position:absolute;left:129px;top:0;width:548px;height:72px;background:var(--navy);border-radius:0 0 22px 22px;color:var(--yellow);font-weight:500;font-size:27px;display:flex;align-items:center;justify-content:center}
  .headline{position:absolute;left:0;top:86px;width:805px;text-align:center;font-family:"Oswald",Impact,sans-serif;font-weight:600;font-size:58px;line-height:64px;color:var(--white);text-shadow:0 3px 0 var(--navy),0 0 6px rgba(10,30,110,.6)}
  .cert-pill{position:absolute;left:209px;top:238px;width:384px;height:41px;background:var(--orange);border-radius:21px;color:var(--white);font-weight:500;font-size:29px;display:flex;align-items:center;justify-content:center}
  .license-seal{position:absolute;left:50px;top:239px;width:116px;height:116px;border-radius:50%;background:var(--red);border:3px solid var(--orange);box-shadow:0 3px 6px rgba(0,0,0,.35);color:var(--white);font-weight:700;font-size:24px;line-height:24px;display:flex;align-items:center;justify-content:center;text-align:center;transform:rotate(-24deg)}
  .schedule-bubble{position:absolute;left:598px;top:258px;width:190px;height:120px;background:var(--cloud);border:3px solid var(--white);border-radius:60px 70px 60px 55px;box-shadow:0 3px 6px rgba(0,0,0,.2);color:var(--navy);font-weight:500;font-size:24px;line-height:26px;display:flex;align-items:center;justify-content:center;text-align:center;transform:rotate(15deg)}
  .brand-art{position:absolute;left:200px;top:385px;width:380px;height:210px;border-radius:110px;background:radial-gradient(ellipse at center,#c9f0ff 0%,#7fd3fb 70%,rgba(127,211,251,0) 100%)}
  .brand-name{position:absolute;left:0;top:455px;width:805px;text-align:center;font-weight:900;font-size:64px;line-height:70px;color:var(--navy)}
  .deco-triangle{position:absolute;left:30px;top:528px}
  .deco-ring{position:absolute;left:680px;top:486px;width:124px;height:124px;border-radius:50%;border:5px solid var(--orange)}
  .photo{position:absolute;left:432px;top:612px;width:373px;height:365px;background:linear-gradient(90deg,rgba(255,255,255,1) 0%,rgba(240,226,210,.85) 30%,#e8d6c2 60%,#dcc6ae 100%)}
  .services{position:absolute;left:52px;top:697px;list-style:none}
  .services li{position:relative;padding-left:38px;color:var(--ink);font-weight:500;font-size:29px;line-height:33px;margin-bottom:15px;border-bottom:1px solid rgba(27,58,155,.12);width:520px}
  .services li svg{position:absolute;left:0;top:4px}
  .footer-wave{position:absolute;left:0;top:962px;width:805px;height:40px}
  .footer{position:absolute;left:0;top:993px;width:805px;height:134px;background:var(--yellow)}
  .cta-pill{position:absolute;left:194px;top:968px;width:415px;height:38px;background:var(--navy);border-radius:19px;color:var(--white);font-family:"Roboto Slab",Georgia,serif;font-weight:700;font-size:20px;display:flex;align-items:center;justify-content:center}
  .phone{position:absolute;left:36px;top:1013px;display:flex;align-items:center;gap:12px;color:var(--ink);font-weight:900;font-size:62px;line-height:66px}
  .address{position:absolute;left:36px;top:1082px;display:flex;align-items:center;gap:14px;color:var(--navy);font-weight:500;font-size:22px}
  .divider{position:absolute;left:543px;top:1025px;width:2px;height:80px;background:var(--orange)}
  .social{position:absolute;left:566px;top:1042px;width:239px;height:44px;background:var(--red);border-radius:22px 0 0 22px;color:var(--white);font-weight:500;font-size:24px;display:flex;align-items:center;padding-left:20px;gap:10px}
  .social .dot{width:20px;height:20px;border-radius:50%;border:3px solid var(--white)}

  /* Spanish side */
  .flyer--es .age-tab{background:var(--yellow);color:var(--navy)}
  .flyer--es .headline{font-size:54px;text-shadow:0 3px 0 #8e0f12,0 0 6px rgba(110,10,10,.6)}
  .flyer--es .cert-pill{left:142px;width:521px;background:var(--navy);font-size:23px}
  .flyer--es .license-seal{background:var(--orange);border-color:var(--red-deep);color:var(--navy);font-size:19px;line-height:19px;font-weight:500;transform:rotate(-18deg)}
  .flyer--es .schedule-bubble{font-size:18px;line-height:20px;padding:0 16px}
  .flyer--es .photo{background:linear-gradient(90deg,rgba(255,255,255,1) 0%,rgba(236,232,226,.85) 30%,#e2dbd1 60%,#d6c8b6 100%)}
  .flyer--es .footer{background:var(--navy)}
  .flyer--es .cta-pill{background:var(--orange)}
  .flyer--es .phone{color:var(--white)}
  .flyer--es .address{color:var(--white)}
  .flyer--es .divider{background:rgba(255,255,255,.5)}
  .flyer--es .social{background:var(--aqua)}
</style>
</head>
<body>

<!-- English side -->
<main class="flyer flyer--en" lang="en">
  <svg class="backdrop" viewBox="0 0 805 500" aria-hidden="true">
    <defs>
      <linearGradient id="skyFill" x1="0" y1="0" x2="1" y2="1">
        <stop offset="0" stop-color="#1f9cf5"/>
        <stop offset="1" stop-color="#1c4fc9"/>
      </linearGradient>
    </defs>
    <path d="M0 0H805V380Q720 365 650 420Q560 490 400 490Q240 490 160 420Q100 375 0 382Z" fill="var(--orange)"/>
    <path d="M0 0H805V368Q720 352 650 408Q560 478 400 478Q240 478 160 408Q100 362 0 370Z" fill="url(#skyFill)"/>
  </svg>

  <div class="age-tab">Children from 6 Weeks to 12 years old</div>
  <h1 class="headline">Accepting All the Programs<br>( TPB, OMW) and Private</h1>
  <div class="cert-pill">CPR &amp; First Aid Certified</div>
  <div class="license-seal">NYC<br>Licensed</div>
  <div class="schedule-bubble">Full Time<br>Part Time and<br>After School</div>

  <div class="brand-art" role="img" aria-label="Cartoon children beside the daycare name"></div>
  <div class="brand-name">Lumo Kid Care</div>

  <svg class="deco-triangle" width="56" height="50" viewBox="0 0 56 50" aria-hidden="true">
    <path d="M4 4H52L28 46Z" fill="none" stroke="#29b6f6" stroke-width="5" stroke-linejoin="round"/>
  </svg>
  <div class="deco-ring"></div>

  <div class="photo" role="img" aria-label="Photo of a young girl playing with wooden dinosaur toys"></div>

  <ul class="services">
    <li><svg width="28" height="28" viewBox="0 0 24 24"><path d="M12 1l3.2 7 7.6.8-5.7 5.1 1.6 7.5L12 17.6 5.3 21.4l1.6-7.5L1.2 8.8 8.8 8z" fill="var(--orange)"/></svg>Provide Homework<br>Assistance</li>
    <li><svg width="28" height="28" viewBox="0 0 24 24"><path d="M12 1l3.2 7 7.6.8-5.7 5.1 1.6 7.5L12 17.6 5.3 21.4l1.6-7.5L1.2 8.8 8.8 8z" fill="var(--orange)"/></svg>Potty Training</li>
    <li><svg width="28" height="28" viewBox="0 0 24 24"><path d="M12 1l3.2 7 7.6.8-5.7 5.1 1.6 7.5L12 17.6 5.3 21.4l1.6-7.5L1.2 8.8 8.8 8z" fill="var(--orange)"/></svg>Outdoor Activities</li>
    <li><svg width="28" height="28" viewBox="0 0 24 24"><path d="M12 1l3.2 7 7.6.8-5.7 5.1 1.6 7.5L12 17.6 5.3 21.4l1.6-7.5L1.2 8.8 8.8 8z" fill="var(--orange)"/></svg>Nutritional Meals &amp; Snack</li>
    <li><svg width="28" height="28" viewBox="0 0 24 24"><path d="M12 1l3.2 7 7.6.8-5.7 5.1 1.6 7.5L12 17.6 5.3 21.4l1.6-7.5L1.2 8.8 8.8 8z" fill="var(--orange)"/></svg>Baby Wipes</li>
  </ul>

  <div class="footer"></div>
  <svg class="footer-wave" viewBox="0 0 805 40" preserveAspectRatio="none" aria-hidden="true">
    <path d="M0 20Q12 8 24 20T48 20T72 20T96 20T120 20T144 20T168 20T192 20T216 20T240 20T264 20T288 20T312 20T336 20T360 20T384 20T408 20T432 20T456 20T480 20T504 20T528 20T552 20T576 20T600 20T624 20T648 20T672 20T696 20T720 20T744 20T768 20T792 20T816 20" fill="none" stroke="var(--navy)" stroke-width="4"/>
    <path d="M0 31H805V40H0Z" fill="var(--yellow)"/>
  </svg>
  <div class="cta-pill">Get More Details, Contact Us Today!</div>

  <div class="phone">
    <svg width="32" height="32" viewBox="0 0 24 24" aria-hidden="true"><circle cx="12" cy="12" r="12" fill="var(--white)"/><path d="M8.5 5.5l2 3-1.3 1.2c.7 1.7 2 3 3.6 3.7l1.2-1.3 3 2-.8 2.3c-4.8-.2-9.5-4.9-9.8-9.7z" fill="var(--orange)"/></svg>
    555-718-2043
  </div>
  <div class="address">
    <svg width="22" height="28" viewBox="0 0 22 28" aria-hidden="true"><path d="M11 1C5.5 1 1.5 5 1.5 10.2 1.5 17 11 27 11 27s9.5-10 9.5-16.8C20.5 5 16.5 1 11 1z" fill="var(--white)"/><circle cx="11" cy="10.5" r="3.6" fill="var(--orange)"/></svg>
    582 E 416th ST, APT 4C, Bronx, NY, 10587
  </div>
  <div class="divider"></div>
  <div class="social"><span class="dot"></span>@lumokidcare</div>
</main>

<!-- Spanish side -->
<main class="flyer flyer--es" lang="es">
  <svg class="backdrop" viewBox="0 0 805 500" aria-hidden="true">
    <defs>
      <linearGradient id="redFill" x1="0" y1="0" x2="1" y2="1">
        <stop offset="0" stop-color="#f0302a"/>
        <stop offset="1" stop-color="#c8161a"/>
      </linearGradient>
    </defs>
    <path d="M0 0H805V380Q720 365 650 420Q560 490 400 490Q240 490 160 420Q100 375 0 382Z" fill="var(--orange)"/>
    <path d="M0 0H805V368Q720 352 650 408Q560 478 400 478Q240 478 160 408Q100 362 0 370Z" fill="url(#redFill)"/>
  </svg>

  <div class="age-tab">Niños de 6 semanas a 12 años</div>
  <h1 class="headline">Aceptando Todos los Programas<br>(TPB, OMW) y Privado</h1>
  <div class="cert-pill">Certificación en CPR y Primeros Auxilios</div>
  <div class="license-seal">Licencia<br>por el<br>estado<br>de NY</div>
  <div class="schedule-bubble">Tiempo completo, tiempo parcial y después de la escuela</div>

  <div class="brand-art" role="img" aria-label="Niños de caricatura junto al nombre de la guardería"></div>
  <div class="brand-name">Lumo Kid Care</div>

  <svg class="deco-triangle" width="56" height="50" viewBox="0 0 56 50" aria-hidden="true">
    <path d="M4 4H52L28 46Z" fill="none" stroke="#29b6f6" stroke-width="5" stroke-linejoin="round"/>
  </svg>
  <div class="deco-ring"></div>

  <div class="photo" role="img" aria-label="Foto de un niño sonriente jugando con juguetes de madera"></div>

  <ul class="services">
    <li><svg width="28" height="28" viewBox="0 0 24 24"><path d="M12 1l3.2 7 7.6.8-5.7 5.1 1.6 7.5L12 17.6 5.3 21.4l1.6-7.5L1.2 8.8 8.8 8z" fill="var(--orange)"/></svg>Actividades al aire libre</li>
    <li><svg width="28" height="28" viewBox="0 0 24 24"><path d="M12 1l3.2 7 7.6.8-5.7 5.1 1.6 7.5L12 17.6 5.3 21.4l1.6-7.5L1.2 8.8 8.8 8z" fill="var(--orange)"/></svg>Asistencia con la tarea</li>
    <li><svg width="28" height="28" viewBox="0 0 24 24"><path d="M12 1l3.2 7 7.6.8-5.7 5.1 1.6 7.5L12 17.6 5.3 21.4l1.6-7.5L1.2 8.8 8.8 8z" fill="var(--orange)"/></svg>Entrenamiento para ir al baño</li>
    <li><svg width="28" height="28" viewBox="0 0 24 24"><path d="M12 1l3.2 7 7.6.8-5.7 5.1 1.6 7.5L12 17.6 5.3 21.4l1.6-7.5L1.2 8.8 8.8 8z" fill="var(--orange)"/></svg>Desayunos, Comidas y<br>refrigerios nutricionales</li>
    <li><svg width="28" height="28" viewBox="0 0 24 24"><path d="M12 1l3.2 7 7.6.8-5.7 5.1 1.6 7.5L12 17.6 5.3 21.4l1.6-7.5L1.2 8.8 8.8 8z" fill="var(--orange)"/></svg>Toallitas para bebé</li>
  </ul>

  <div class="footer"></div>
  <svg class="footer-wave" viewBox="0 0 805 40" preserveAspectRatio="none" aria-hidden="true">
    <path d="M0 20Q12 8 24 20T48 20T72 20T96 20T120 20T144 20T168 20T192 20T216 20T240 20T264 20T288 20T312 20T336 20T360 20T384 20T408 20T432 20T456 20T480 20T504 20T528 20T552 20T576 20T600 20T624 20T648 20T672 20T696 20T720 20T744 20T768 20T792 20T816 20" fill="none" stroke="var(--navy)" stroke-width="4"/>
    <path d="M0 31H805V40H0Z" fill="var(--navy)"/>
  </svg>
  <div class="cta-pill">Get More Details, Contact Us Today!</div>

  <div class="phone">
    <svg width="32" height="32" viewBox="0 0 24 24" aria-hidden="true"><circle cx="12" cy="12" r="12" fill="var(--white)"/><path d="M8.5 5.5l2 3-1.3 1.2c.7 1.7 2 3 3.6 3.7l1.2-1.3 3 2-.8 2.3c-4.8-.2-9.5-4.9-9.8-9.7z" fill="var(--navy)"/></svg>
    555-718-2043
  </div>
  <div class="address">
    <svg width="22" height="28" viewBox="0 0 22 28" aria-hidden="true"><path d="M11 1C5.5 1 1.5 5 1.5 10.2 1.5 17 11 27 11 27s9.5-10 9.5-16.8C20.5 5 16.5 1 11 1z" fill="var(--white)"/><circle cx="11" cy="10.5" r="3.6" fill="var(--navy)"/></svg>
    582 E 416th ST, APT 4C, Bronx, NY, 10587
  </div>
  <div class="divider"></div>
  <div class="social"><span class="dot"></span>@lumokidcare</div>
</main>

</body>
</html>
```